Lomi-Seret - Promote and Support a community

Design a website for Ethiopean Community. the design should be friendly, easy to navigate and maintain the look & feel of the Ethiopian culture. a proposed logo is attached but it can be change according to your recommendations. This is a project we are doing at a discount rate as it supports a weak community.
Please visit their current website http://www.lomi-seret.example.il/index.php?lang=en

Target Market(s)

Community members, potential doners

Industry/Entity Type

community

Number of Pages Required

1 page

Font styles to use
Sans Serif

Requirements
Must have
• easy to navigate friendly interface

```html
<!DOCTYPE html>
<html lang="en">
<head>
<meta charset="utf-8">
<title>Lomi-Seret</title>
<link href="https://fonts.googleapis.com/css2?family=Roboto:wght@400;500;700&display=swap" rel="stylesheet">
<style>
:root{
  --red:#7d0000;
  --red-dark:#6a0000;
  --cream:#faf1d9;
  --gold:#d3b73c;
  --gold-light:#e9c64c;
  --green:#1d8a5e;
  --green-btn:#22845a;
  --ink:#2b2b2b;
  --white:#fff;
}
*{box-sizing:border-box;margin:0;padding:0}
html,body{width:1200px;height:3775px;overflow:hidden}
body{font-family:'Roboto',sans-serif;color:var(--ink);background:var(--white);position:relative}
.abs{position:absolute}
section,header,footer{position:absolute;left:0;width:1200px}

/* header */
.topbar{top:0;height:48px;background:var(--white)}
.call{right:248px;top:10px;color:var(--green);font-weight:500;font-size:21px;display:flex;align-items:center;gap:6px}
.lang{right:118px;top:12px;font-size:15px;font-weight:500;color:var(--red);display:flex;align-items:center;gap:8px}
.flag{width:22px;height:22px;border-radius:50%;background:#2b3a8c;display:inline-block}
.navbar{top:48px;height:53px;background:var(--red)}
.nav{right:72px;top:0;height:53px;display:flex;align-items:center;gap:30px;list-style:none}
.nav li{color:var(--white);font-size:15px;font-weight:500}
.nav li.active{color:var(--gold-light);border-bottom:2px solid var(--gold-light);padding-bottom:3px}
.brand{left:109px;top:0;width:124px;height:124px;border-radius:50%;background:var(--white);border:3px solid var(--red);display:flex;align-items:center;justify-content:center;z-index:3;font-weight:700;color:var(--red);font-size:16px;text-align:center}

/* hero */
.hero{top:101px;height:510px;background:linear-gradient(120deg,#9c7a55 0%,#b84a5a 30%,#5a7fb0 55%,#d9a34a 75%,#c0462f 100%)}
.hero h1{left:0;width:1200px;top:150px;text-align:center;color:var(--white);font-size:48px;font-weight:700;text-shadow:0 2px 6px rgba(0,0,0,.4)}
.btn{display:flex;align-items:center;justify-content:center;color:var(--white);font-weight:700;text-transform:uppercase}
.hero .btn{left:508px;top:240px;width:185px;height:52px;background:var(--green-btn);font-size:21px}
.dots{left:566px;top:370px;display:flex;gap:12px}
.dots span{width:15px;height:15px;border-radius:50%;border:2px solid var(--white)}
.dots span:first-child{background:var(--white)}
.torn{left:0;width:1200px}

/* welcome */
.welcome{top:608px;height:501px;background:var(--cream)}
.h2{font-size:30px;font-weight:700;text-transform:uppercase}
.welcome .h2{left:111px;top:100px;color:var(--red)}
.welcome p{left:111px;top:164px;width:482px;font-size:15px;line-height:18.5px;text-align:justify}
.welcome .btn{left:111px;top:327px;width:160px;height:57px;background:var(--red);font-size:19px;box-shadow:4px 4px 6px rgba(0,0,0,.25)}
.welcome .art{left:632px;top:52px;width:466px;height:366px;border-radius:40% 55% 45% 50%;background:radial-gradient(circle at 40% 40%,#d8c08e,#c35a7a 55%,#3c8fa0 80%,transparent 82%)}

/* community */
.community{top:1109px;height:563px;background:var(--red)}
.community .h2{left:111px;top:102px;color:var(--white)}
.community h3{left:111px;top:165px;width:380px;color:var(--gold-light);font-size:25px;font-weight:500;line-height:31px}
.community p{left:111px;top:250px;width:380px;color:var(--white);font-size:15px;line-height:18.5px}
.link{font-weight:700;font-size:19px;border-bottom:3px solid currentColor;padding-bottom:4px}
.community .link{left:111px;top:380px;color:var(--gold-light)}
.community .frame{left:734px;top:54px;width:396px;height:466px;border:2px solid var(--gold)}
.community .art{left:599px;top:108px;width:490px;height:381px;background:linear-gradient(135deg,#e9d9b8,#35a49d 35%,#e25a77 60%,#f2c23c 85%)}

/* programs */
.programs{top:1672px;height:903px;background:var(--white)}
.programs .h2{left:0;width:1200px;top:62px;text-align:center;color:var(--red)}
.card{background:var(--white);box-shadow:0 2px 10px rgba(0,0,0,.18)}
.feature{left:111px;top:168px;width:435px;height:565px}
.feature .art{left:4px;top:3px;width:430px;height:344px;background:linear-gradient(180deg,#b64a3c,#5da6b3 45%,#e9e4dc 75%,#8a3b2a)}
.feature h4{left:22px;top:365px;color:var(--red);font-size:24px;font-weight:500}
.feature p{left:22px;top:405px;width:392px;font-size:15px;line-height:18.5px;text-align:justify}
.feature .link{left:24px;top:500px;color:var(--red)}
.mini{left:557px;width:529px;height:182px}
.mini .art{left:4px;top:3px;width:258px;height:176px}
.mini h4{left:281px;top:26px;color:var(--red);font-size:16px;font-weight:500}
.mini p{left:282px;top:60px;width:200px;font-size:12.5px;line-height:16px}
.mini .link{left:282px;top:132px;color:var(--red);font-size:18px}
.programs>.btn{left:520px;top:789px;width:158px;height:56px;background:var(--red);font-size:19px;box-shadow:4px 4px 6px rgba(0,0,0,.25)}

/* support */
.support{top:2575px;height:351px;background:var(--gold)}
.support .h2{left:0;width:1200px;top:70px;text-align:center;color:var(--white)}
.support p{left:210px;width:780px;top:121px;text-align:center;color:var(--white);font-size:15px;line-height:18.5px}
.support .btn{left:507px;top:231px;width:186px;height:49px;background:var(--red);font-size:21px}

/* partners */
.partners{top:2926px;height:490px;background:var(--cream)}
.partners .h2{left:0;width:1200px;top:52px;text-align:center;color:var(--red)}
.partner{top:174px;width:206px;height:171px;background:var(--white);border:2px solid #e2dccd;display:flex;align-items:center;justify-content:center}
.partner i{display:block;width:90px;height:90px;border-radius:14px}
.arrow{top:239px}

/* footer */
.footer{top:3399px;height:376px;background:var(--green);color:var(--white)}
.footer h5{font-size:25px;font-weight:500}
.about{left:111px;top:90px}
.about p{width:300px;font-size:15px;line-height:18.5px;margin-top:0}
.about .lead{margin-top:36px;margin-bottom:14px}
.about .line{margin-bottom:8px}
.flogo{left:514px;top:86px;width:170px;height:170px;border-radius:50%;background:var(--white);border:3px solid var(--red);display:flex;align-items:center;justify-content:center;color:var(--red);font-weight:700;font-size:20px}
.contact{left:869px;top:90px}
.contact ul{list-style:none;margin-top:28px}
.contact li{display:flex;gap:18px;align-items:flex-start;font-size:15px;line-height:18px;margin-bottom:20px}
.contact svg{flex:none}
.rule{left:0;top:322px;width:1200px;height:1px;background:rgba(255,255,255,.4)}
.copy{left:0;width:1200px;top:341px;text-align:center;font-size:15px}
</style>
</head>
<body>

<header class="topbar">
  <div class="abs call">
    <svg width="24" height="24" viewBox="0 0 24 24"><path fill="currentColor" d="M6.6 10.8a15 15 0 0 0 6.6 6.6l2.2-2.2a1 1 0 0 1 1-.25 11.4 11.4 0 0 0 3.6.6 1 1 0 0 1 1 1V20a1 1 0 0 1-1 1A17 17 0 0 1 3 4a1 1 0 0 1 1-1h3.5a1 1 0 0 1 1 1c0 1.25.2 2.45.6 3.6a1 1 0 0 1-.25 1z"/></svg>
    CALL:04-555-0142
  </div>
  <div class="abs lang">English <span class="flag"></span>
    <svg width="16" height="10" viewBox="0 0 16 10"><path d="M1 1l7 7 7-7" stroke="var(--red)" stroke-width="2" fill="none"/></svg>
  </div>
</header>
<div class="abs brand">Lomi-Seret</div>
<nav class="navbar abs" style="left:0;width:1200px">
  <ul class="nav abs">
    <li class="active">Home</li><li>About</li><li>The Community</li><li>Programs</li><li>News</li><li>Advocacy</li><li>Partners</li><li>Support Us</li>
  </ul>
</nav>

<section class="hero">
  <div class="abs" role="img" aria-label="Colourful hand-woven Ethiopian baskets" style="inset:0"></div>
  <h1 class="abs">WELCOME TO LOMI-SERET</h1>
  <div class="abs btn">Support us</div>
  <div class="abs dots"><span></span><span></span><span></span></div>
</section>
<svg class="abs torn" style="top:580px" height="34" viewBox="0 0 1200 34" preserveAspectRatio="none"><path fill="#faf1d9" d="M0 22 L40 16 80 24 120 14 170 22 210 12 260 20 300 15 350 24 400 13 450 21 500 16 550 25 600 14 650 22 700 12 750 21 800 15 850 24 900 13 950 20 1000 12 1050 21 1100 14 1150 22 1200 10 V34 H0Z"/></svg>

<section class="welcome">
  <h2 class="abs h2">Welcome to Lomi Seret</h2>
  <p class="abs">Aliyah (immigration) from Ethiopia to Israel and the transition to a sedentary lifestyle has resulted in the emergence of chronic diseases, in particular diabetes. While only 0.4% of the new immigrants were diagnosed with Type 2 diabetes upon arrival, by the time they had lived in Israel for ten years the figure had risen to 18% - three times as many as in the general population. The incidence of hypertension, obesity, asthma and Type 1 diabetes had also increased dramatically.</p>
  <div class="abs btn">Read more</div>
  <div class="abs art" role="img" aria-label="Woven baskets arranged in the shape of Ethiopia"></div>
</section>

<section class="community">
  <h2 class="abs h2">The Community</h2>
  <h3 class="abs">Health &amp; the Ethiopian Israeli Community</h3>
  <p class="abs">Today the Ethiopian Israeli community numbers over a 120,000 with new immigrants still continuing to arrive. For many, immigration led to the disintegration of to a traditional family and social structures with traumatic results for the community and further impeding absorp tion into Israeli society.</p>
  <span class="abs link">Read More :</span>
  <div class="abs frame"></div>
  <div class="abs art" role="img" aria-label="Close-up of striped woven basket lids"></div>
</section>

<section class="programs">
  <h2 class="abs h2">Programs</h2>
  <div class="abs card feature">
    <div class="abs art" role="img" aria-label="Community members in white robes gathered in a decorated hall"></div>
    <h4 class="abs">Health &amp; Education Presentations</h4>
    <p class="abs">Lorem ipsum dolor sit amet, consectetur adipiscing elit, sed do eiusmod tempor incididunt ut labore et dolore magna aliqua. Quis ipsum suspendisse ultrices gravida. Risus commodo viverra</p>
    <span class="abs link">Read More :</span>
  </div>
  <div class="abs card mini" style="top:168px">
    <div class="abs art" role="img" aria-label="Traditional dish served on injera" style="background:linear-gradient(135deg,#d33d6c,#e8c37a 50%,#4a2a1a)"></div>
    <h4 class="abs">Nutrition &amp; Cookery Courses</h4>
    <p class="abs">Within the Ethiopian community, women and mothers play a vital role inam provides women with basic health and disease</p>
    <span class="abs link">Read More :</span>
  </div>
  <div class="abs card mini" style="top:360px">
    <div class="abs art" role="img" aria-label="Ceremony with ornate umbrellas in smoke" style="background:linear-gradient(135deg,#3aa7a0,#c9b79a 50%,#6c5a45)"></div>
    <h4 class="abs">Research &amp; Data Collection</h4>
    <p class="abs">Within the Ethiopian community, women and mothers play a vital role inam provides women with basic health and disease</p>
    <span class="abs link">Read More :</span>
  </div>
  <div class="abs card mini" style="top:553px">
    <div class="abs art" role="img" aria-label="Evening gathering by the water under coloured flags" style="background:linear-gradient(180deg,#1c2a33,#3f6b4e 50%,#142027)"></div>
    <h4 class="abs">Amharic Radio Program</h4>
    <p class="abs">Within the Ethiopian community, women and mothers play a vital role inam provides women with basic health and disease</p>
    <span class="abs link">Read More :</span>
  </div>
  <div class="abs btn">Read more</div>
</section>

<section class="support">
  <h2 class="abs h2">Support Us</h2>
  <p class="abs">Lomi Seret non-profit organization operates to promote the ethiopian israel community healthcato a re, using donations and govermant funding. Seret has public to a us institue donation approval (Income Tax instruction, section 46).To support the to organization, please send a check to "Lomi Seret" to the address: 4 Ridge Lane, Mail Box 1200, Midtown.Please submit you name and address for invoice.</p>
  <div class="abs btn">Support us</div>
</section>

<section class="partners">
  <h2 class="abs h2">Our Partners</h2>
  <svg class="abs arrow" style="left:16px" width="28" height="44" viewBox="0 0 28 44"><path d="M24 4L6 22l18 18" stroke="#111" stroke-width="4" fill="none"/></svg>
  <div class="abs partner" style="left:116px"><i style="background:#2a4f9e"></i></div>
  <div class="abs partner" style="left:363px"><i style="background:#3fb0c9"></i></div>
  <div class="abs partner" style="left:630px"><i style="background:#2f7fc2"></i></div>
  <div class="abs partner" style="left:879px"><i style="background:#4aa84e"></i></div>
  <svg class="abs arrow" style="left:1152px" width="28" height="44" viewBox="0 0 28 44"><path d="M4 4l18 18L4 40" stroke="#111" stroke-width="4" fill="none"/></svg>
</section>
<svg class="abs torn" style="top:3386px" height="30" viewBox="0 0 1200 30" preserveAspectRatio="none"><path fill="#1d8a5e" d="M0 14 L40 8 80 16 120 6 170 14 210 4 260 12 300 7 350 16 400 5 450 13 500 8 550 17 600 6 650 14 700 4 750 13 800 7 850 16 900 5 950 12 1000 4 1050 13 1100 6 1150 14 1200 8 V30 H0Z"/></svg>

<footer class="footer">
  <div class="abs about">
    <h5>LOMI SERET</h5>
    <p class="lead">Lomi means health in Amharic, and also signifies a jewel basket: an expensive and unique gift to preserve.</p>
    <p class="line">Seret means health in Hebrew.</p>
    <p>Health is a gift to be preserved</p>
  </div>
  <div class="abs flogo">Lomi-Seret</div>
  <div class="abs contact">
    <h5>contact</h5>
    <ul>
      <li><svg width="28" height="28" viewBox="0 0 24 24"><path fill="none" stroke="#fff" stroke-width="1.5" d="M6.6 10.8a15 15 0 0 0 6.6 6.6l2.2-2.2a1 1 0 0 1 1-.25 11.4 11.4 0 0 0 3.6.6 1 1 0 0 1 1 1V20a1 1 0 0 1-1 1A17 17 0 0 1 3 4a1 1 0 0 1 1-1h3.5a1 1 0 0 1 1 1c0 1.25.2 2.45.6 3.6a1 1 0 0 1-.25 1z"/></svg><span style="padding-top:6px">04-5550142</span></li>
      <li><svg width="28" height="32" viewBox="0 0 24 28"><path fill="none" stroke="#fff" stroke-width="1.5" d="M12 26s9-9 9-15a9 9 0 0 0-18 0c0 6 9 15 9 15z"/><circle cx="12" cy="11" r="3.5" fill="none" stroke="#fff" stroke-width="1.5"/></svg><span>Ridge Lane 4/2 POB 1200<br>Midtown, 10450</span></li>
      <li><svg width="28" height="22" viewBox="0 0 28 22"><rect x="1" y="1" width="26" height="20" rx="2" fill="none" stroke="#fff" stroke-width="1.5"/><path d="M1 3l13 10L27 3" fill="none" stroke="#fff" stroke-width="1.5"/></svg><span style="padding-top:2px">hello@lomi-seret.example.il</span></li>
    </ul>
  </div>
  <div class="abs rule"></div>
  <div class="abs copy">Copyright © 2022 Lomi Seret</div>
</footer>

</body>
</html>
```